Real State Agency App

We need an app design for a real state agency, we provide mockups for our project that ilustrates very well what we need
our web site is www.brindlevaleestates.com,

Target Market(s)

Tourism

Font styles to use
Other font styles liked:
• attached you will find it

Requirements
Must have
• Colors like the logo

```html
<!DOCTYPE html>
<html lang="en">
<head>
<meta charset="utf-8">
<title>Brindlevale – Property App Screens</title>
<link href="https://fonts.googleapis.com/css2?family=Source+Sans+3:wght@400;600&display=swap" rel="stylesheet">
<style>
:root{
  --pink:#ec6aa8;
  --violet:#a477c8;
  --blue:#3a90e4;
  --purple:#8c6fc9;
  --white:#ffffff;
  --ink:#7c7c8c;
  --muted:#b9b9c4;
  --line:#dcdce4;
  --canvas:#ffffff;
  --app-gradient:linear-gradient(180deg,var(--pink) 0%,var(--violet) 45%,var(--blue) 100%);
  --badge-gradient:linear-gradient(135deg,var(--blue),var(--pink));
}
*{box-sizing:border-box;margin:0;padding:0}
html,body{width:1200px;height:1200px;overflow:hidden;background:var(--canvas)}
body{position:relative;font-family:"Source Sans 3",sans-serif;color:var(--white)}
.screen{position:absolute;width:242px;height:526px;border-radius:30px;overflow:hidden;background:var(--app-gradient)}
.screen--menu{left:94px;top:104px}
.screen--search{left:802px;top:88px}
.screen--sell{left:444px;top:574px}
.abs{position:absolute}
.status{top:14px;left:17px;right:17px;display:flex;justify-content:space-between;font-size:7px;letter-spacing:.2px}
.status__signal{display:flex;align-items:center;gap:4px}
.battery{width:11px;height:5px;border:1px solid var(--white);border-radius:1px;background:var(--white);background-clip:content-box;padding:1px}

.brand{display:flex;align-items:center}
.brand__dot{width:28px;height:28px;border-radius:50%;background:var(--blue);position:relative;z-index:1;box-shadow:0 2px 4px rgba(0,0,0,.15)}
.brand__name{background:var(--white);color:var(--ink);font-size:14px;height:28px;line-height:28px;padding:0 10px 0 18px;margin-left:-12px;letter-spacing:.3px}

.badge{width:26px;height:26px;border-radius:50%;background:var(--badge-gradient);display:flex;align-items:center;justify-content:center;box-shadow:0 2px 5px rgba(0,0,0,.18)}
.badge svg{width:12px;height:12px}

/* menu screen */
.menu{left:40px;top:150px;width:161px;height:227px;border:1px solid rgba(255,255,255,.35)}
.menu__rule{left:0;right:0;height:1px;background:rgba(255,255,255,.35)}
.menu__item{left:0;right:0;text-align:center;font-size:9px;letter-spacing:.5px}
.menu__item--big{font-size:10.5px}
.menu__item--active{background:var(--white);color:var(--purple);height:26px;line-height:26px}

/* language */
.lang-tip{left:70px;width:102px;height:50px;background:var(--white);padding:8px 7px;color:var(--ink)}
.lang-tip::after{content:"";position:absolute;left:50px;bottom:-5px;border:5px solid transparent;border-bottom:0;border-top-color:var(--white)}
.lang-tip__title{font-size:4.5px;color:var(--blue);letter-spacing:.3px}
.lang-tip__text{font-size:4.5px;margin-top:3px;line-height:1.2}
.lang-tip__close{position:absolute;right:5px;top:5px;font-size:5px;color:var(--muted)}
.lang-tip__btn{position:absolute;right:7px;bottom:8px;background:var(--blue);color:var(--white);font-size:4px;padding:1px 7px}
.lang{left:29px;width:183px;height:20px;display:flex;border:1px solid rgba(255,255,255,.7)}
.lang__opt{flex:1;display:flex;align-items:center;justify-content:center;gap:4px;font-size:6.5px;letter-spacing:.6px}
.lang__opt--on{background:var(--white);color:var(--blue)}
.lang__radio{width:8px;height:8px;border-radius:50%;border:2px solid var(--blue);background:var(--white)}

/* cards */
.card{left:42px;width:158px;background:var(--white);color:var(--ink)}
.card__title{left:0;right:0;text-align:center;font-size:10px;color:var(--purple);letter-spacing:.3px}
.card__rule{left:0;right:0;height:1px;background:var(--line)}
.field{left:26px;right:26px;height:1px;background:var(--line)}
.field--on{background:var(--violet)}
.field__label{left:26px;font-size:3.8px;color:var(--ink)}
.field__value{left:26px;font-size:6px;color:var(--purple)}
.chevron{right:28px;width:4px;height:4px;border-right:1px solid var(--muted);border-bottom:1px solid var(--muted);transform:rotate(45deg)}
.button{left:26px;right:26px;background:var(--purple);color:var(--white);font-size:7px;text-align:center;letter-spacing:.4px;box-shadow:0 2px 4px rgba(0,0,0,.15)}

/* sell screen */
.topbar{left:0;right:0;top:0;height:63px;background:var(--pink)}
.topbar .brand__dot{width:20px;height:20px}
.topbar .brand__name{height:19px;line-height:19px;font-size:10px;padding:0 8px 0 14px;margin-left:-10px}
.hero{left:0;right:0;top:63px;height:133px;background:linear-gradient(100deg,#a9c4d8 0%,#b7cad6 50%,#d9cdb6 78%,#c9a884 100%)}
.hero-lower{left:0;right:0;top:196px;bottom:0;background:linear-gradient(180deg,#a177c9 0%,#6f84d6 45%,var(--blue) 100%)}
.mini{width:12px;height:12px;border-radius:50%;background:var(--badge-gradient)}
.lorem{left:26px;right:26px;top:206px;font-size:6px;line-height:1.25;color:var(--muted)}
.help{left:86px;width:71px;height:11px;background:var(--white);color:var(--ink);font-size:4.5px;text-align:center;line-height:11px}
.nav{height:18px;background:var(--white);color:var(--ink);font-size:6px;display:flex;align-items:center;gap:6px;letter-spacing:.4px}
.nav--back{left:0;width:77px;border-radius:0 10px 10px 0;padding-left:7px}
.nav--next{right:0;width:80px;border-radius:10px 0 0 10px;padding-left:8px}
</style>
</head>
<body>

<!-- Menu screen -->
<section class="screen screen--menu">
  <div class="abs status"><span>10:00 AM</span><span class="status__signal">4G <span class="battery"></span></span></div>
  <div class="abs brand" style="left:62px;top:55px"><span class="brand__dot"></span><span class="brand__name">Brindlevale</span></div>

  <nav class="abs menu">
    <div class="abs badge" style="left:67px;top:-14px"><svg viewBox="0 0 12 12" fill="none" stroke="#fff" stroke-width="1.2"><circle cx="5" cy="5" r="3.5"/><path d="M7.6 7.6 10.5 10.5"/></svg></div>
    <div class="abs menu__item menu__item--big" style="top:24px">Search Property</div>
    <div class="abs menu__rule" style="top:41px"></div>
    <div class="abs menu__rule" style="top:77px"></div>
    <div class="abs menu__item" style="top:85px">Our Service</div>
    <div class="abs menu__item menu__item--active" style="top:103px">Sell Property</div>
    <div class="abs menu__item" style="top:136px">Contact Us</div>
    <div class="abs menu__rule" style="top:154px"></div>
    <div class="abs menu__rule" style="top:187px"></div>
    <div class="abs menu__item menu__item--big" style="top:191px">Add Property</div>
    <div class="abs badge" style="left:67px;top:213px"><svg viewBox="0 0 12 12" fill="none" stroke="#fff" stroke-width="1"><path d="M6 1v10M1 6h10"/></svg></div>
  </nav>

  <div class="abs lang-tip" style="top:419px">
    <div class="lang-tip__title">CHANGE LANGUAGE</div>
    <div class="lang-tip__text">You can change<br>your language any time !!</div>
    <span class="lang-tip__close">×</span>
    <span class="lang-tip__btn">Got it</span>
  </div>
  <div class="abs lang" style="top:476px">
    <span class="lang__opt">SPAIN</span>
    <span class="lang__opt lang__opt--on">ENGLISH <span class="lang__radio"></span></span>
    <span class="lang__opt">GERMAN</span>
  </div>
</section>

<!-- Search screen -->
<section class="screen screen--search">
  <div class="abs status"><span>10:00 AM</span><span class="status__signal">4G <span class="battery"></span></span></div>
  <div class="abs brand" style="left:63px;top:56px"><span class="brand__dot"></span><span class="brand__name">Brindlevale</span></div>

  <div class="abs card" style="top:151px;height:226px">
    <div class="abs badge" style="left:66px;top:-15px"><svg viewBox="0 0 12 12" fill="none" stroke="#fff" stroke-width="1.2"><circle cx="5" cy="5" r="3.5"/><path d="M7.6 7.6 10.5 10.5"/></svg></div>
    <div class="abs card__title" style="top:29px">Search Property</div>
    <div class="abs card__rule" style="top:46px"></div>
    <div class="abs field__value" style="top:62px">For Rent</div>
    <div class="abs chevron" style="top:63px"></div>
    <div class="abs field field--on" style="top:70px"></div>
    <div class="abs field__label" style="top:72px">To Reform</div>
    <div class="abs field" style="top:94px"></div>
    <div class="abs field__label" style="top:96px">Key</div>
    <div class="abs chevron" style="top:109px"></div>
    <div class="abs field" style="top:115px"></div>
    <div class="abs field__label" style="top:118px">Type</div>
    <div class="abs chevron" style="top:131px"></div>
    <div class="abs field" style="top:137px"></div>
    <div class="abs field__label" style="top:140px">Area</div>
    <div class="abs button" style="top:183px;height:20px;line-height:20px">Search Properties</div>
  </div>

  <div class="abs lang-tip" style="top:419px">
    <div class="lang-tip__title">CHANGE LANGUAGE</div>
    <div class="lang-tip__text">You can change<br>your language any time !!</div>
    <span class="lang-tip__close">×</span>
    <span class="lang-tip__btn">Got it</span>
  </div>
  <div class="abs lang" style="top:476px">
    <span class="lang__opt">SPAIN</span>
    <span class="lang__opt lang__opt--on">ENGLISH <span class="lang__radio"></span></span>
    <span class="lang__opt">GERMAN</span>
  </div>
</section>

<!-- Sell screen -->
<section class="screen screen--sell">
  <div class="abs topbar"></div>
  <div class="abs status"><span>10:00 AM</span><span class="status__signal">4G <span class="battery"></span></span></div>
  <svg class="abs" style="left:14px;top:43px" width="14" height="9" viewBox="0 0 14 9" stroke="#fff" stroke-width="1"><path d="M0 .5h14M0 4.5h14M0 8.5h14"/></svg>
  <div class="abs brand" style="left:83px;top:37px"><span class="brand__dot"></span><span class="brand__name">Brindlevale</span></div>
  <svg class="abs" style="left:220px;top:42px" width="10" height="10" viewBox="0 0 12 12" fill="none" stroke="#fff" stroke-width="1.1"><circle cx="5" cy="5" r="4"/><path d="M8 8 11.5 11.5"/></svg>

  <div class="abs hero" role="img" aria-label="Photo of a house with a gabled roof against a pale sky"></div>
  <div class="abs hero-lower"></div>
  <span class="abs mini" style="left:13px;top:76px"></span>
  <span class="abs mini" style="left:13px;top:95px"></span>

  <div class="abs card" style="top:150px;height:279px">
    <div class="abs badge" style="left:66px;top:-15px"><svg viewBox="0 0 12 12" fill="none" stroke="#fff" stroke-width="1"><path d="M2 6 6 2.5 10 6M3 5.2V10h6V5.2"/></svg></div>
    <div class="abs card__title" style="top:29px">Sell Property</div>
    <div class="abs card__rule" style="top:46px"></div>
    <p class="abs lorem" style="top:56px">Lorem Ipsum is simply dummy text of the printing and typesetting industry. Lorem Ipsum has been the industry's standard dummy text ever since the 1500s,</p>
    <div class="abs field__value" style="top:115px">Aria Collins</div>
    <div class="abs field field--on" style="top:124px"></div>
    <div class="abs field__label" style="top:127px">Name</div>
    <div class="abs field" style="top:142px"></div>
    <div class="abs field__label" style="top:145px">Surname</div>
    <div class="abs field" style="top:160px"></div>
    <div class="abs field__label" style="top:164px">Phone</div>
    <div class="abs field" style="top:179px"></div>
    <div class="abs field__label" style="top:183px">Email</div>
    <div class="abs field" style="top:198px"></div>
    <div class="abs field__label" style="top:200px">Property Name</div>
    <div class="abs field" style="top:217px"></div>
    <div class="abs field__label" style="top:219px">Property Information</div>
    <div class="abs button" style="top:237px;height:18px;line-height:18px">Sell Property</div>
  </div>
  <div class="abs badge" style="left:108px;top:415px"><svg viewBox="0 0 12 12" fill="none" stroke="#fff" stroke-width="1"><path d="M2 2.5h8v5H5l-2.5 2v-2H2z"/></svg></div>
  <div class="abs help" style="top:447px">Any Help? We are here</div>

  <div class="abs nav nav--back" style="top:480px">
    <svg width="8" height="6" viewBox="0 0 8 6" fill="none" stroke="currentColor" stroke-width=".8"><path d="M8 3H1M3 .5 .8 3 3 5.5"/></svg>Back to Home
  </div>
  <div class="abs nav nav--next" style="top:480px">
    <svg width="8" height="6" viewBox="0 0 8 6" fill="none" stroke="currentColor" stroke-width=".8"><path d="M0 3h7M5 .5 7.2 3 5 5.5"/></svg>Next to Confirm
  </div>
</section>

</body>
</html>
```